Refer a Friend A5 Flyer for Healthcare Staff

We need an A5 flyer that we can hand out to existing and new staff members promoting our Refer a friend Scheme. We need the leaflet to encourage staff to talk to their family and friends about joining our Healthcare Agency, which provides staff to local care related establishments. Using our logo and brand colours blue and green, as per our website, the final design will need to clearly convey the benefits and attractions of referring additional staff to the team. In addition is the promotion of our SocialHub page, requesting staff to like the page and to like and share various posts.

Target Market(s)

Healthcare and potential Healthcare Staff

Industry/Entity Type

Healthcare

Colors
33b8a4
3277b5

Requirements
Must have
• Company Logo, Brand colours,
• text; "Refer a Friend and receive a £50 Bonus after just 1 completed shift"
• text; "3 easy steps to refer a friend, 1 Fill out your name on the back of your Business Card 2 Hand the card to your friend or any person you wish to refer, 3 ask your friend to present the card to us when they attend their interview"
• text; "Like and share any of our Open Days on SocialHub for a chance to win a prize, you can find us easily by searching @CarewellPlacementGroup"
• text; "Like our Page to stay up to date with our events and offers"
Nice to have
• care worker / elderly care / support worker pictures
• Content / pics from website www.carewellplacementgroup.co.uk

```html
<!DOCTYPE html>
<html lang="en">
<head>
<meta charset="utf-8">
<title>Refer a Friend Flyer – Carewell Placement</title>
<link href="https://fonts.googleapis.com/css2?family=Poppins:wght@400;500;600;700;800&display=swap" rel="stylesheet">
<style>
  :root {
    --brand-teal: #33b8a4;
    --brand-blue: #3277b5;
    --panel-blue: #4a86c2;
    --panel-blue-light: #5b97cf;
    --ink-grey: #5a5a5a;
    --body-grey: #666666;
    --soft-grey: #f1f2f2;
    --paper: #ffffff;
    --backdrop: #e4e6e8;
    --brand-navy: #1f3f7a;
  }
  * { box-sizing: border-box; margin: 0; padding: 0; }
  html, body {
    width: 1200px; height: 1000px; overflow: hidden;
    background: var(--backdrop);
    font-family: "Poppins", sans-serif;
  }
  .flyer {
    position: absolute; left: 275px; top: 40px;
    width: 650px; height: 920px;
    background: var(--paper);
    overflow: hidden;
  }
  .hero {
    position: absolute; left: 0; top: 0; width: 650px; height: 463px;
    background:
      radial-gradient(ellipse at 35% 55%, #eef2f5 0 18%, transparent 40%),
      radial-gradient(ellipse at 80% 70%, #dfeee0 0 20%, transparent 45%),
      linear-gradient(160deg, #5f8f3e 0%, #8fbf63 35%, #cfe3b8 65%, #eef4e6 100%);
  }
  .brand {
    position: absolute; right: 44px; top: 56px;
    display: flex; align-items: center; gap: 8px;
  }
  .brand-dot {
    width: 14px; height: 14px; border-radius: 50%;
    background: var(--brand-teal);
  }
  .brand-name {
    font-weight: 500; font-size: 22px; color: var(--brand-navy);
    line-height: 1;
  }
  .offer {
    position: absolute; left: 0; top: 463px; width: 325px; height: 220px;
    padding: 32px 0 0 44px;
  }
  .offer-lead {
    font-weight: 700; font-size: 37px; line-height: 1.05;
    color: var(--brand-teal); letter-spacing: -1.4px;
  }
  .offer-amount {
    font-weight: 800; font-size: 45px; line-height: 1.05;
    color: var(--brand-blue); letter-spacing: -2.4px; margin-top: 2px;
  }
  .offer-terms {
    font-weight: 600; font-size: 19.5px; color: var(--ink-grey);
    letter-spacing: -0.9px; margin-top: 2px;
  }
  .social {
    position: absolute; left: 0; top: 683px; width: 325px; height: 237px;
    background: var(--soft-grey);
    padding: 44px 0 0 44px;
  }
  .social-body, .social-cta {
    width: 238px;
    font-size: 15.2px; line-height: 1.22;
  }
  .social-body { color: var(--body-grey); }
  .social-cta { color: var(--brand-blue); margin-top: 24px; }
  .steps {
    position: absolute; left: 325px; top: 463px; width: 325px; height: 457px;
    background: linear-gradient(160deg, var(--panel-blue) 0%, var(--panel-blue-light) 100%);
    color: #fff;
    padding: 50px 0 0 37px;
  }
  .steps-title {
    font-weight: 700; font-size: 29.5px; line-height: 1.2; letter-spacing: -0.3px;
  }
  .step {
    position: absolute; left: 38px; display: flex; align-items: center; gap: 16px;
  }
  .step-icon {
    width: 56px; height: 56px; border-radius: 50%;
    background: var(--brand-teal);
    display: flex; align-items: center; justify-content: center; flex: none;
  }
  .step-text {
    font-size: 14.4px; line-height: 1.15; width: 162px;
  }
  .step-1 { top: 157px; }
  .step-2 { top: 253px; }
  .step-3 { top: 349px; }
</style>
</head>
<body>
  <main class="flyer">
    <div class="hero" role="img" aria-label="Photo of a smiling care worker in a white uniform embracing an elderly woman in a wheelchair in a sunny park"></div>
    <div class="brand">
      <span class="brand-dot"></span>
      <span class="brand-name">Carewell Placement</span>
    </div>

    <section class="offer">
      <h1 class="offer-lead">Refer a Friend<br>and receive a</h1>
      <p class="offer-amount">£50 BONUS</p>
      <p class="offer-terms">after just 1 completed shift</p>
    </section>

    <section class="social">
      <p class="social-body">Like and share any of our Open Days on SocialHub for a chance to win a prize, you can find us easily by searching @CarewellPlacementGroup</p>
      <p class="social-cta">Like our Page to stay up to date with our events and offers</p>
    </section>

    <section class="steps" role="img" aria-label="Faded photo of care staff behind the referral steps">
      <h2 class="steps-title">3 easy steps to<br>refer a friend</h2>

      <div class="step step-1">
        <span class="step-icon">
          <svg width="28" height="28" viewBox="0 0 28 28" fill="none" stroke="#fff" stroke-width="1.6" stroke-linecap="round" stroke-linejoin="round">
            <path d="M18 14V4H6v20h8"/>
            <path d="M9 9h6M9 13h6M9 17h3"/>
            <path d="M16 23l1-3 6-6 2 2-6 6z"/>
          </svg>
        </span>
        <p class="step-text">Fill out your name on the back of your Business Card</p>
      </div>

      <div class="step step-2">
        <span class="step-icon">
          <svg width="30" height="28" viewBox="0 0 30 28" fill="none" stroke="#fff" stroke-width="1.6" stroke-linecap="round" stroke-linejoin="round">
            <rect x="12" y="5" width="14" height="10" rx="1" transform="rotate(-20 19 10)"/>
            <path d="M3 12h3v9H3M6 13l5-2 5 4-2 2-3-2M6 20h4l7 3"/>
          </svg>
        </span>
        <p class="step-text">Hand the card to your friend or any person you wish to refer</p>
      </div>

      <div class="step step-3">
        <span class="step-icon">
          <svg width="30" height="28" viewBox="0 0 30 28" fill="none" stroke="#fff" stroke-width="1.6" stroke-linecap="round" stroke-linejoin="round">
            <circle cx="9" cy="7" r="3"/>
            <circle cx="21" cy="7" r="3"/>
            <path d="M4 18v-4a5 5 0 0 1 10 0v4M16 18v-4a5 5 0 0 1 10 0v4"/>
            <path d="M2 19h26M6 19v6M24 19v6"/>
          </svg>
        </span>
        <p class="step-text">3 ask your friend to present the card to us when they attend their interview</p>
      </div>
    </section>
  </main>
</body>
</html>
```